Marijuana Lifestyle Multi-Shop Brand Website

We need a website that provides an online retail shop for our products, along with the additional functionality:

Main Page: Slider with great photography (we are still looking for a professional photographer to take photos for us.

Shop Tab: E-commerce site.
- Main Categories:
- Accessories
- Bubblers
- Dry Pieces
- Scientific Glass
- Water Pipes
- Custom Shop
- University Store

Stores/Resellers: This is a store look-up, so people can enter their zipcode and find our resellers and partners.

Brand Partners: Just a basic filter and page so that we can highlight our partners and why we've selected them.

Contact Us: Basic Form
- Career Page: Basic Page

About Us: Basic Page

Blog:

Search Bar:

Essentially, we want a near exact copy of this website, but with our brand, logo and content. https://corkwillowbins.com/

This site is really really simple, but we like simple.

Our reserved domain address is: www.runbaketend.com

About Us:
We are multi-shop for marijuana-related accessories. We sell quality glass pipes, vaporizers, amazing storage options, dime bags, custom t-shirts and other stuff.

We have a network of resellers that allow us to put in micro-installations into gift shops, convenience stores, tobacco stores, etc. and we are trying to change the overall perception that buying these items should be mainstream and as transparent as going to the Fen or the Walnut Shop.

I've attached a logo that should give you an idea of our color scheme. We don't have our photography yet for the slider
Updates

As an FYI, for the e-commerce part of my website, I already have a license for WP SwiftTill.

Industry/Entity Type

Shop

```html
<!DOCTYPE html>
<html lang="en">
<head>
<meta charset="utf-8">
<title>Cart – oakhaven</title>
<link href="https://fonts.googleapis.com/css2?family=Arimo:wght@400;700&family=Open+Sans:wght@400;700;800&display=swap" rel="stylesheet">
<style>
:root{
  --stage:#000;
  --topbar:#232323;
  --header:#1b1b1b;
  --titlebar:#191919;
  --main:#1c1c1c;
  --line:#333;
  --line-soft:#2c2c2c;
  --text:#e6e6e6;
  --muted:#8a8a8a;
  --green:#87a10a;
  --green-text:#8fa52a;
  --star:#f7d61b;
  --star-off:#888;
  --scroll:#e8e8e8;
}
*{box-sizing:border-box;margin:0;padding:0}
html,body{width:1200px;height:1000px;overflow:hidden;background:var(--stage)}
body{position:relative;font-family:"Arimo",Arial,sans-serif;color:var(--text);font-size:11px}
.site{position:absolute;left:0;top:163px;width:1190px;height:677px;background:var(--main);overflow:hidden}
.scrollbar{position:absolute;left:1190px;top:163px;width:10px;height:677px;background:var(--scroll)}
.scrollbar span{position:absolute;left:2px;top:6px;width:6px;height:455px;background:#c4c4c4;border-radius:3px}

.topbar{position:absolute;left:0;top:0;width:100%;height:24px;background:var(--topbar);border-bottom:1px solid #2e2e2e}
.social{position:absolute;left:199px;top:0;display:flex;height:24px}
.social li{list-style:none;width:23px;height:24px;border-right:1px solid #383838;display:flex;align-items:center;justify-content:center}
.social li:first-child{border-left:1px solid #383838}
.social i{display:block;width:7px;height:7px;border-radius:50%;background:#8a8a8a}
.topnav{position:absolute;right:209px;top:0;height:24px;display:flex;align-items:center;font-size:8px;font-weight:700;color:#bbb}
.topnav a{color:#bbb;text-decoration:none;padding:0 8px;border-right:1px solid #444;line-height:10px}
.topnav span{padding-left:8px}

.header{position:absolute;left:0;top:24px;width:100%;height:87px;background:var(--header);border-bottom:1px solid var(--line)}
.brand{position:absolute;left:212px;top:12px;display:flex;align-items:center;gap:10px}
.brand i{width:60px;height:60px;border-radius:50%;background:var(--green)}
.brand b{font-family:"Open Sans",sans-serif;font-weight:700;font-size:30px;color:#a9bd4b;letter-spacing:-.5px}
.mainnav{position:absolute;right:209px;top:0;height:87px;display:flex;align-items:center;font-size:10px;color:#999}
.mainnav a{color:#999;text-decoration:none;margin-left:22px}
.mainnav a.active{color:#fff}
.mainnav svg{margin-left:22px}
.cartbtn{position:absolute;left:1156px;top:25px;width:36px;height:36px;border:1px solid #3a3a3a;background:#121212;display:flex;align-items:center;justify-content:center}

.titlebar{position:absolute;left:0;top:111px;width:100%;height:44px;background:var(--titlebar);border-bottom:1px solid var(--line)}
.titlebar h1{position:absolute;left:207px;top:14px;font-size:12px;font-weight:400;color:#eee}
.crumbs{position:absolute;right:211px;top:17px;font-size:8px;color:#ccc}

.sidebar-rule{position:absolute;left:779px;top:155px;width:1px;height:522px;background:var(--line)}

.cart{position:absolute;left:207px;top:192px;width:534px;border-collapse:collapse;font-size:9.5px}
.cart th,.cart td{border:1px solid var(--line);height:42px;padding:0 9px;text-align:left}
.cart th{height:28px;font-family:"Open Sans",sans-serif;font-weight:700;font-size:9px;letter-spacing:1px;color:#fff}
.cart .product a{color:var(--green-text);text-decoration:none}
.cart .dim{color:#999}
.remove{display:block;width:11px;height:11px;border-radius:50%;background:#e4ecc4;position:relative}
.remove:after{content:"×";position:absolute;left:0;top:-3px;width:11px;text-align:center;font-size:11px;font-weight:700;color:var(--green)}
.thumb{display:block;width:24px;height:24px;border:1px solid #555;background:linear-gradient(#777,#4a4a4a)}
.qty{display:flex;margin:0 auto;width:97px;height:32px;border:1px solid #3a3a3a}
.qty span{width:32px;display:flex;align-items:center;justify-content:center;background:linear-gradient(#2a2a2a,#050505);color:#ddd}
.qty span.n{width:33px;background:#1a1a1a;color:#bbb;border-left:1px solid #3a3a3a;border-right:1px solid #3a3a3a}
.actions td{height:84px;position:relative}
.coupon{position:absolute;left:9px;top:7px;width:150px;height:31px;border:1px solid #444;background:#151515;font-size:8px;font-weight:700;color:#aaa;padding:10px 9px}
.btn{position:absolute;height:32px;background:var(--green);color:#fff;font-size:8.5px;display:flex;align-items:center;justify-content:center}

h3{font-family:"Open Sans",sans-serif;font-weight:800;font-size:10.5px;letter-spacing:.8px;color:#fff;position:absolute}
.totals{position:absolute;left:207px;top:467px;width:256px;border-collapse:collapse;font-size:9.5px}
.totals td{border:1px solid var(--line);padding:0 18px;height:26px}
.totals td:last-child{text-align:right;padding:0 18px 0 0;width:88px}
.totals .lbl{font-family:"Open Sans",sans-serif;font-weight:700;letter-spacing:1.2px;font-size:9px}
.totals .dimrow td{height:41px;color:#888;line-height:16px}
.totals .grand{color:var(--green-text);font-weight:700}

.side{position:absolute;left:817px;width:165px}
.search{top:225px;display:flex;height:30px}
.search div{flex:1;border:1px solid #444;background:#151515;font-size:8.5px;color:#aaa;padding:9px 4px}
.search span{width:36px;background:var(--green);color:#fff;font-size:8.5px;display:flex;align-items:center;justify-content:center}
.cats{top:288px;list-style:none;font-size:8.5px;color:#aaa}
.cats li{height:18px;padding-left:8px;position:relative}
.cats li:before{content:"";position:absolute;left:0;top:3px;border-left:3px solid #888;border-top:2px solid transparent;border-bottom:2px solid transparent}
.cats em{font-size:7px}
.rated{top:396px;list-style:none}
.rated li{height:67px;border-top:1px solid #2e2e2e;position:relative;padding-top:8px}
.rated b{font-size:8.5px;color:#bbb}
.rated .thumb{position:absolute;right:5px;top:11px;width:20px;height:20px}
.stars{display:flex;gap:1px;margin-top:14px}
.rated small{display:block;font-size:7.5px;color:#999;margin-top:2px}
</style>
</head>
<body>
<svg width="0" height="0" style="position:absolute">
  <defs>
    <symbol id="star" viewBox="0 0 10 10"><polygon points="5,0.4 6.4,3.5 9.7,3.7 7.2,5.9 8,9.4 5,7.5 2,9.4 2.8,5.9 0.3,3.7 3.6,3.5"/></symbol>
  </defs>
</svg>

<div class="site">
  <div class="topbar">
    <ul class="social" aria-label="Social links">
      <li><i></i></li><li><i></i></li><li><i></i></li><li><i></i></li><li><i></i></li><li><i></i></li>
    </ul>
    <nav class="topnav">
      <a>HOME</a><a>About Us</a><a>My Account</a><a>Shop</a><a>Career Page</a><a>Blog</a><a>Contact Us</a>
      <span>+1 800 555 0142 / info@runbaketend.com</span>
    </nav>
  </div>

  <header class="header">
    <div class="brand"><i></i><b>oakhaven</b></div>
    <nav class="mainnav">
      <a>HOME</a><a>About Us</a><a class="active">My Account</a><a>Shop</a><a>Career Page</a><a>Blog</a><a>Contact Us</a>
      <svg width="10" height="10" viewBox="0 0 10 10"><circle cx="4" cy="4" r="3" fill="none" stroke="#999" stroke-width="1.4"/><line x1="6.2" y1="6.2" x2="9.3" y2="9.3" stroke="#999" stroke-width="1.6"/></svg>
    </nav>
    <div class="cartbtn"><svg width="12" height="11" viewBox="0 0 12 11"><path d="M0 1h2l2 6h6l1.5-4.5H3" fill="#fff"/><circle cx="5" cy="9.5" r="1.2" fill="#fff"/><circle cx="9" cy="9.5" r="1.2" fill="#fff"/></svg></div>
  </header>

  <div class="titlebar">
    <h1>Cart</h1>
    <div class="crumbs">You are here: &nbsp;Home &nbsp;/ &nbsp;Cart</div>
  </div>

  <div class="sidebar-rule"></div>

  <table class="cart">
    <tr><th style="width:46px"></th><th style="width:62px"></th><th style="width:100px">PRODUCT</th><th style="width:77px">PRICE</th><th style="width:169px">QUANTITY</th><th>TOTAL</th></tr>
    <tr><td><span class="remove"></span></td><td><span class="thumb" role="img" aria-label="Product 1 thumbnail"></span></td><td class="product"><a>Product 1</a></td><td>$50.00</td><td><div class="qty"><span>-</span><span class="n">2</span><span>+</span></div></td><td>$100.00</td></tr>
    <tr><td><span class="remove"></span></td><td><span class="thumb" role="img" aria-label="Product 3 thumbnail"></span></td><td class="product"><a>Product 3</a></td><td class="dim">$149.99</td><td><div class="qty"><span>-</span><span class="n">1</span><span>+</span></div></td><td class="dim">$149.99</td></tr>
    <tr><td><span class="remove"></span></td><td><span class="thumb" role="img" aria-label="Product 2 thumbnail"></span></td><td class="product"><a>Product 2</a></td><td>$99.99</td><td><div class="qty"><span>-</span><span class="n">1</span><span>+</span></div></td><td>$99.99</td></tr>
    <tr class="actions"><td colspan="6">
      <div class="coupon">Coupon code</div>
      <div class="btn" style="left:167px;top:7px;width:150px">Apply Coupon</div>
      <div class="btn" style="left:386px;top:7px;width:137px">Update Cart</div>
      <div class="btn" style="left:386px;top:44px;width:137px">Proceed to Checkout</div>
    </td></tr>
  </table>

  <h3 style="left:207px;top:448px">CART TOTALS</h3>
  <h3 style="left:484px;top:448px">CALCULATE SHIPPING</h3>
  <table class="totals">
    <tr><td class="lbl">CART SUBTOTAL</td><td>$349.98</td></tr>
    <tr class="dimrow"><td class="lbl">SHIPPING AND<br>HANDLING</td><td>Free<br>Shipping</td></tr>
    <tr><td class="lbl">ORDER TOTAL</td><td class="grand">$349.98</td></tr>
  </table>

  <h3 style="left:817px;top:206px">SEARCH PRODUCTS</h3>
  <div class="side search"><div>Search for products</div><span>Search</span></div>

  <h3 style="left:817px;top:267px">PRODUCT CATEGORIES</h3>
  <ul class="side cats">
    <li>Accessories <em>(1)</em></li><li>Bubblers <em>(1)</em></li><li>Custom Shop <em>(1)</em></li><li>Dry Pieces <em>(1)</em></li>
  </ul>

  <h3 style="left:817px;top:379px">TOP RATED PRODUCTS</h3>
  <ul class="side rated">
    <li><b>Product 4</b><span class="thumb" role="img" aria-label="Product 4 thumbnail"></span>
      <div class="stars"><svg width="58" height="10"><use href="#star" width="10" height="10" fill="#f7d61b"/><use href="#star" x="12" width="10" height="10" fill="#f7d61b"/><use href="#star" x="24" width="10" height="10" fill="#f7d61b"/><use href="#star" x="36" width="10" height="10" fill="#f7d61b"/><use href="#star" x="48" width="10" height="10" fill="#f7d61b"/></svg></div><small>$199.99</small></li>
    <li><b>Product 1</b><span class="thumb" role="img" aria-label="Product 1 thumbnail"></span>
      <div class="stars"><svg width="58" height="10"><use href="#star" width="10" height="10" fill="#f7d61b"/><use href="#star" x="12" width="10" height="10" fill="#f7d61b"/><use href="#star" x="24" width="10" height="10" fill="#f7d61b"/><use href="#star" x="36" width="10" height="10" fill="#f7d61b"/><use href="#star" x="48" width="10" height="10" fill="#f7d61b"/></svg></div><small>$50.00</small></li>
    <li><b>Product 3</b><span class="thumb" role="img" aria-label="Product 3 thumbnail"></span>
      <div class="stars"><svg width="58" height="10"><use href="#star" width="10" height="10" fill="#f7d61b"/><use href="#star" x="12" width="10" height="10" fill="#f7d61b"/><use href="#star" x="24" width="10" height="10" fill="#f7d61b"/><use href="#star" x="36" width="10" height="10" fill="#f7d61b"/><use href="#star" x="48" width="10" height="10" fill="#888"/></svg></div><small>$149.99</small></li>
    <li><b>Product 2</b><span class="thumb" role="img" aria-label="Product 2 thumbnail"></span>
      <div class="stars"><svg width="58" height="10"><use href="#star" width="10" height="10" fill="#f7d61b"/><use href="#star" x="12" width="10" height="10" fill="#f7d61b"/><use href="#star" x="24" width="10" height="10" fill="#f7d61b"/><use href="#star" x="36" width="10" height="10" fill="#f7d61b"/><use href="#star" x="48" width="10" height="10" fill="#888"/></svg></div><small>$99.99</small></li>
  </ul>
</div>
<div class="scrollbar"><span></span></div>
</body>
</html>
```